Business Card Design Project

beauty / make up / lashes

Industry/Entity Type

Business

Contact Information for Business Card

pink / gold / wait / black vintage classic elegant design

```html
<!DOCTYPE html>
<html lang="en">
<head>
<meta charset="utf-8">
<title>Business Card – Front and Back</title>
<link rel="stylesheet" href="https://fonts.googleapis.com/css2?family=Questrial&display=swap">
<style>
  :root {
    --magenta: #e5048c;
    --magenta-deep: #b8086f;
    --ink: #050505;
    --gold: #f2c318;
    --gold-deep: #d9901a;
    --paper: #ffffff;
    --stage: #ecebea;
  }
  * { margin: 0; padding: 0; box-sizing: border-box; }
  html, body {
    width: 1200px;
    height: 1200px;
    overflow: hidden;
    background: var(--stage);
    font-family: "Questrial", "Century Gothic", sans-serif;
  }
  .sheet {
    position: relative;
    width: 1200px;
    height: 1200px;
  }
  .card {
    position: absolute;
    left: 170px;
    width: 860px;
    height: 491px;
    overflow: hidden;
    background: var(--ink);
    box-shadow: 0 10px 30px rgba(0,0,0,0.18);
  }
  .card--front { top: 80px; }
  .card--back { top: 629px; }
  .card__art {
    position: absolute;
    inset: 0;
    width: 100%;
    height: 100%;
  }
  .company-name {
    position: absolute;
    color: var(--paper);
    font-size: 52px;
    font-weight: 400;
    letter-spacing: 0.5px;
    line-height: 1;
    white-space: nowrap;
  }
  .card--front .company-name { left: 48px; top: 64px; }
  .card--back .company-name { left: 48px; top: 250px; }

  .contact {
    position: absolute;
    left: 390px;
    top: 282px;
    list-style: none;
    color: var(--paper);
    font-size: 24px;
    line-height: 1.2;
  }
  .contact__item {
    display: flex;
    align-items: flex-start;
    gap: 10px;
  }
  .contact__item--address { margin-bottom: 16px; }
  .contact__icon {
    flex: 0 0 18px;
    width: 18px;
    height: 18px;
    margin-top: 5px;
    fill: var(--magenta);
  }
  .contact__lines { display: flex; flex-direction: column; }
</style>
</head>
<body>
<main class="sheet">

  <section class="card card--front" aria-label="Business card front">
    <svg class="card__art" viewBox="0 0 860 491" xmlns="http://www.w3.org/2000/svg">
      <defs>
        <radialGradient id="splash-ink" cx="50%" cy="50%" r="50%">
          <stop offset="0%" stop-color="var(--ink)"/>
          <stop offset="45%" stop-color="var(--ink)" stop-opacity="0.85"/>
          <stop offset="100%" stop-color="var(--ink)" stop-opacity="0"/>
        </radialGradient>
        <radialGradient id="splash-pink-gold" cx="45%" cy="50%" r="50%">
          <stop offset="0%" stop-color="var(--magenta)"/>
          <stop offset="50%" stop-color="var(--magenta-deep)" stop-opacity="0.8"/>
          <stop offset="75%" stop-color="var(--gold)" stop-opacity="0.45"/>
          <stop offset="100%" stop-color="var(--gold)" stop-opacity="0"/>
        </radialGradient>
      </defs>
      <rect class="base" width="860" height="491" fill="var(--ink)"/>
      <path class="wave-band" d="M0 0 H860 V400 C790 330 700 260 560 228 C440 200 300 205 170 218 C100 225 40 226 0 222 Z" fill="var(--magenta)"/>
      <rect role="img" aria-label="Black ink splash ornament" x="640" y="50" width="220" height="200" fill="url(#splash-ink)"/>
      <rect role="img" aria-label="Pink ink splash with gold leaf ornament" x="0" y="290" width="320" height="201" fill="url(#splash-pink-gold)"/>
    </svg>

    <h1 class="company-name">company name</h1>

    <ul class="contact">
      <li class="contact__item contact__item--address">
        <svg class="contact__icon" viewBox="0 0 18 18"><path d="M9 1a6 6 0 0 0-6 6c0 4.5 6 10 6 10s6-5.5 6-10a6 6 0 0 0-6-6zm0 8.3A2.3 2.3 0 1 1 9 4.7a2.3 2.3 0 0 1 0 4.6z"/></svg>
        <span>company address</span>
      </li>
      <li class="contact__item">
        <svg class="contact__icon" viewBox="0 0 18 18"><path d="M4.5 1.5l3 3-1.8 2.2a10 10 0 0 0 5.6 5.6l2.2-1.8 3 3-2 2.5C8 15.5 2.5 10 2 3.5z"/></svg>
        <span class="contact__lines"><span>0123 45 678</span><span>0111 22 33 4455</span></span>
      </li>
      <li class="contact__item">
        <svg class="contact__icon" viewBox="0 0 18 18"><path d="M1 4h16v10H1z M1 4l8 6 8-6" fill="var(--magenta)" stroke="var(--ink)" stroke-width="1.2"/></svg>
        <span>email@Companyname.com</span>
      </li>
      <li class="contact__item">
        <svg class="contact__icon" viewBox="0 0 18 18"><circle cx="9" cy="9" r="8"/><path d="M1 9h16M9 1c-3 3-3 13 0 16M9 1c3 3 3 13 0 16" stroke="var(--ink)" stroke-width="1.1" fill="none"/></svg>
        <span>www.companyname.com</span>
      </li>
    </ul>
  </section>

  <section class="card card--back" aria-label="Business card back">
    <svg class="card__art" viewBox="0 0 860 491" xmlns="http://www.w3.org/2000/svg">
      <defs>
        <radialGradient id="floral-gold" cx="55%" cy="55%" r="50%">
          <stop offset="0%" stop-color="var(--gold)"/>
          <stop offset="40%" stop-color="var(--gold-deep)" stop-opacity="0.8"/>
          <stop offset="70%" stop-color="var(--magenta-deep)" stop-opacity="0.5"/>
          <stop offset="100%" stop-color="var(--magenta)" stop-opacity="0"/>
        </radialGradient>
      </defs>
      <rect class="base" width="860" height="491" fill="var(--ink)"/>
      <circle class="disc" cx="790" cy="300" r="330" fill="var(--magenta)"/>
      <rect role="img" aria-label="Gold floral vine ornament over dark pink ink splashes" x="480" y="60" width="380" height="340" fill="url(#floral-gold)"/>
    </svg>
    <p class="company-name">company name</p>
  </section>

</main>
</body>
</html>
```